Harbor Stone Holdings Corporate Showcase

Provide an attractive Corporate Website for a boutique Investment Company to showcase our activities and corporate interests.

Our Company works across a number of Sectors including

Real Estate
E-Commerce
Healthcare
Beauty & Personal Care
Technology
Resources

Lets keep the personality

Modern
Global
Sophisticated
Calm
Interesting

Lets keep the pages with MINIMAL Words
Lets use Photos/ Imagery to tell the story

We'll need a Banner Menu -
About Us
Expertise
Global Outlook
Sectors
Management
Media
Contact Us

Many thanks
Best wishes
Simon.

Target Market(s)

Investors
Clients

Coding

Coded - Design and coding required

Number of Pages Required

5+ page

Font styles to use
Sans Serif

Colors
886aae
3176b5
00a990
f68e4d
f04a50
e667a6

Requirements
Must have
• WordPress Coding

Checkout this Website for look and feel - its cool:
www.qvx.example

Harbor Stone Partners
(Harbor Stone Holdings LLP)
London
E9 4PL
United Kingdom

www.HarborStonePartners.example
Nice to have
• Sophisticated colour palette - black/ brown/ blue/ purple/

```html
<!DOCTYPE html>
<html lang="en">
<head>
<meta charset="utf-8">
<title>Harbor Stone Partners</title>
<link rel="stylesheet" href="https://fonts.googleapis.com/css2?family=Libre+Franklin:ital,wght@0,300;0,400;0,500;0,600;1,400&display=swap">
<style>
:root{
  --navy:#0c2a62;
  --mauve:#7f5a7d;
  --plum:#4a2f48;
  --pink:#a8649d;
  --accent:#b23a55;
  --white:#ffffff;
  --soft:#e7dde6;
  --map:#d8d8d8;
}
*{box-sizing:border-box;margin:0;padding:0}
html,body{width:1200px;height:4601px;overflow:hidden}
body{font-family:"Libre Franklin",sans-serif;color:var(--white);position:relative;background:var(--navy)}
.abs{position:absolute}
section{position:absolute;left:0;width:1200px;overflow:hidden}
.photo{position:absolute}
.btn{position:absolute;display:flex;align-items:center;justify-content:center;font-size:11px;font-weight:600;letter-spacing:3.5px;text-transform:uppercase;color:var(--white)}
.btn-fill{background:var(--pink)}
.btn-line{border:1.5px solid var(--white)}
.eyebrow{position:absolute;width:100%;text-align:center;font-size:11px;letter-spacing:2px;font-weight:500;text-transform:uppercase}
.title{position:absolute;width:100%;text-align:center;font-size:31px;font-weight:300}
.para{font-size:12.5px;line-height:24px;font-weight:300}

/* header + hero */
.hero{top:0;height:638px;background:linear-gradient(100deg,#5b5450 0%,#8d8781 35%,#a9a39b 60%,#6d6a60 100%)}
.hero .shade{position:absolute;inset:0;background:rgba(20,20,30,.28)}
.logo{left:93px;top:36px;font-size:22px;font-weight:300}
.nav{left:430px;top:44px;font-size:11px;font-weight:300;display:flex}
.nav a{position:absolute;white-space:nowrap;color:var(--white);text-decoration:none}
.nav a.active{border-top:1px solid var(--accent);padding-top:3px;margin-top:-4px}
.social i{position:absolute;width:9px;height:9px;border-radius:50%;background:var(--white);top:47px}
.hero h1{position:absolute;top:245px;width:100%;text-align:center;font-size:30px;font-weight:400;letter-spacing:.5px}
.hero h2{position:absolute;top:290px;width:100%;text-align:center;font-size:17px;font-weight:300}
.dots span{position:absolute;top:578px;width:32px;height:32px;display:flex;align-items:center;justify-content:center;font-size:12px;border-radius:50%}
.dots .on{background:var(--pink)}

/* about */
.about{top:638px;height:502px;background:var(--navy)}
.about .frame{position:absolute;left:164px;top:55px;width:372px;height:386px;border:1.5px solid var(--accent)}

/* sectors */
.sectors{top:1140px;height:1091px;background:var(--mauve)}
.card h3{position:absolute;font-size:16px;font-weight:400}
.card p{position:absolute;width:315px;font-size:11.5px;line-height:20px;font-weight:300}

/* blog */
.blog{top:2231px;height:954px;background:var(--navy)}
.meta{position:absolute;font-size:9.5px;font-weight:600;letter-spacing:.3px}
.post-title{position:absolute;font-size:24px;font-weight:300}
.blog .para{position:absolute;width:455px;font-size:11.5px;line-height:25px}

/* team */
.team{top:3185px;height:539px;background:var(--mauve)}
.member .bracket{position:absolute;top:117px;width:200px;height:20px;border:2px solid var(--soft);border-bottom:none}
.member .name{position:absolute;top:338px;width:200px;text-align:center;font-size:16px;font-weight:500}
.member .role{position:absolute;top:358px;width:200px;text-align:center;font-size:11px;font-style:italic;font-weight:600}
.member p{position:absolute;top:378px;width:200px;text-align:center;font-size:11.5px;line-height:18px;font-weight:300;padding:0 20px}
.arrow{position:absolute;top:465px;width:30px;height:30px;display:flex;align-items:center;justify-content:center}

/* contact */
.contact{top:3724px;height:506px;background:linear-gradient(135deg,#dcdcdc,#cfcfcf 50%,#d9d9d9)}
.contact .box{position:absolute;left:221px;top:71px;width:758px;height:390px;background:var(--navy)}
.field{position:absolute;border:1px solid #8ea0c4;font-size:12px;padding:9px 7px;font-weight:300}

/* footer */
.footer{top:4230px;height:371px;background:var(--plum)}
.footer h4{position:absolute;top:76px;font-size:14px;font-weight:400}
.footer .link{position:absolute;font-size:12px;font-weight:300}
.footer .rule{position:absolute;left:93px;top:306px;width:1013px;height:1px;background:#6d5269}
.footer .copy{position:absolute;top:327px;width:100%;text-align:center;font-size:11px;font-weight:300;color:#bfaebc}
</style>
</head>
<body>

<section class="hero">
  <div class="photo" role="img" aria-label="Business team meeting around a boardroom table" style="inset:0;background:linear-gradient(100deg,#4f4844 0%,#8c857e 35%,#b0aaa2 60%,#5f6356 100%)"></div>
  <div class="shade"></div>
  <div class="abs logo">Harbor Stone Partners</div>
  <nav class="abs nav">
    <a class="active" style="left:0">About Us</a>
    <a style="left:79px">Expertise</a>
    <a style="left:158px">Global Outlook</a>
    <a style="left:265px">Sectors</a>
    <a style="left:334px">Management</a>
    <a style="left:433px">Media</a>
    <a style="left:495px">Contact Us</a>
  </nav>
  <div class="social"><i style="left:1012px"></i><i style="left:1040px"></i><i style="left:1068px"></i><i style="left:1096px"></i></div>
  <h1>HARBOR STONE HOLDINGS (HSH)</h1>
  <h2>GROWING THE NEXT GENERATION OF BUSINESS</h2>
  <div class="btn btn-fill" style="left:522px;top:348px;width:157px;height:40px">Know More</div>
  <div class="dots"><span class="on" style="left:93px">01</span><span style="left:152px">02</span><span style="left:211px">03</span></div>
</section>

<section class="about">
  <div class="frame"></div>
  <div class="photo" role="img" aria-label="Colleagues meeting in a bright office" style="left:93px;top:28px;width:284px;height:356px;background:linear-gradient(160deg,#eef0f1,#b9bcc0 60%,#5c6270)"></div>
  <div class="photo" role="img" aria-label="Two professionals reviewing a tablet" style="left:354px;top:110px;width:284px;height:359px;background:linear-gradient(160deg,#c8cbc9,#8a7a6a 55%,#3a3636)"></div>
  <div class="abs" style="left:700px;top:97px;font-size:11px;letter-spacing:1.5px;font-weight:600;color:#c98bbd">ABOUT US</div>
  <div class="abs" style="left:700px;top:120px;font-size:30px;font-weight:300">A Few Words About Us</div>
  <p class="abs para" style="left:700px;top:172px;width:340px">Lorem ipsum dolor sit amet, consectetur adipcing elit. Etiam et eros vel ligula malesuada aliquet at quis nunc. Etiam id erat ac libero hendrerit porta. Duis consectetur, tortor ac bibendum condimentum, dolor mi sodales ex, id suscipit mi elit ut odio. Orci varius natoque penatibus et magnis dis parturient montes, nascetur ridiculus mus. Proin quam augue</p>
  <div class="btn btn-fill" style="left:698px;top:357px;width:174px;height:41px">Read More</div>
</section>

<section class="sectors">
  <div class="eyebrow" style="top:29px">Sector</div>
  <div class="title" style="top:57px">Our Sectors</div>

  <div class="card">
    <div class="photo" role="img" aria-label="City skyline model on a desk" style="left:93px;top:116px;width:310px;height:260px;background:linear-gradient(180deg,#cfd6da,#7d8aa0 50%,#4d3e38)"></div>
    <h3 style="left:93px;top:398px">Real Estate</h3>
    <p style="left:93px;top:431px">Lorem ipsum dolor sit amet, cosectetur adipcing elit. Etiam et eros vel ligula malesuada aliquet at quis nunc. Etiam id erat ac libero</p>
    <div class="btn btn-line" style="left:93px;top:510px;width:175px;height:41px">Read More</div>
  </div>
  <div class="card">
    <div class="photo" role="img" aria-label="Cardboard parcels on a laptop keyboard" style="left:445px;top:116px;width:310px;height:260px;background:linear-gradient(160deg,#f1f1f1,#c9a57b 55%,#6b6b6b)"></div>
    <h3 style="left:445px;top:398px">E-Commerce</h3>
    <p style="left:445px;top:431px">Lorem ipsum dolor sit amet, cosectetur adipcing elit. Etiam et eros vel ligula malesuada aliquet at quis nunc. Etiam id erat ac libero</p>
    <div class="btn btn-line" style="left:445px;top:510px;width:175px;height:41px">Read More</div>
  </div>
  <div class="card">
    <div class="photo" role="img" aria-label="Bright hospital corridor" style="left:797px;top:116px;width:310px;height:260px;background:linear-gradient(180deg,#eef2f5,#c7d2dc 60%,#9db0c4)"></div>
    <h3 style="left:797px;top:398px">Healthcare</h3>
    <p style="left:797px;top:431px">Lorem ipsum dolor sit amet, cosectetur adipcing elit. Etiam et eros vel ligula malesuada aliquet at quis nunc. Etiam id erat ac libero</p>
    <div class="btn btn-line" style="left:797px;top:510px;width:175px;height:41px">Read More</div>
  </div>

  <div class="card">
    <div class="photo" role="img" aria-label="Hands with skincare cream and green leaves" style="left:93px;top:596px;width:310px;height:259px;background:linear-gradient(160deg,#f4f6f3,#e3ddd6 60%,#9fbf86)"></div>
    <h3 style="left:93px;top:878px">Beauty &amp; Personal Care</h3>
    <p style="left:93px;top:911px">Lorem ipsum dolor sit amet, cosectetur adipcing elit. Etiam et eros vel ligula malesuada aliquet at quis nunc. Etiam id erat ac libero</p>
    <div class="btn btn-line" style="left:93px;top:990px;width:175px;height:41px">Read More</div>
  </div>
  <div class="card">
    <div class="photo" role="img" aria-label="Hand touching a digital diagram" style="left:445px;top:596px;width:310px;height:259px;background:linear-gradient(160deg,#dfe6ee,#8e9db0 55%,#2f3a4d)"></div>
    <h3 style="left:445px;top:878px">Technology</h3>
    <p style="left:445px;top:911px">Lorem ipsum dolor sit amet, cosectetur adipcing elit. Etiam et eros vel ligula malesuada aliquet at quis nunc. Etiam id erat ac libero</p>
    <div class="btn btn-line" style="left:445px;top:990px;width:175px;height:41px">Read More</div>
  </div>
  <div class="card">
    <div class="photo" role="img" aria-label="Two colleagues talking at a meeting table" style="left:797px;top:596px;width:310px;height:259px;background:linear-gradient(160deg,#eef0ee,#a9aca7 55%,#3c4240)"></div>
    <h3 style="left:797px;top:878px">Resources</h3>
    <p style="left:797px;top:911px">Lorem ipsum dolor sit amet, cosectetur adipcing elit. Etiam et eros vel ligula malesuada aliquet at quis nunc. Etiam id erat ac libero</p>
    <div class="btn btn-line" style="left:797px;top:990px;width:175px;height:41px">Read More</div>
  </div>
</section>

<section class="blog">
  <div class="eyebrow" style="top:33px;color:#c98bbd">Blog</div>
  <div class="title" style="top:62px">Say Media</div>

  <div class="photo" role="img" aria-label="Businessman drawing a growth chart" style="left:93px;top:121px;width:505px;height:356px;background:linear-gradient(120deg,#c9d6e6,#7e92b0 45%,#1e2638)"></div>
  <div class="meta" style="left:629px;top:185px">DEC. 10, 2020 &nbsp;|&nbsp; POSTED BY LOREM</div>
  <div class="post-title" style="left:629px;top:205px">Vestibulum vel dolor sed lacus lobortis</div>
  <p class="para" style="left:629px;top:250px">Phasellus dapibus tincidunt diam in convallis. Nam ac augue sem. Maecenas consectetur magna eget urna eleifend accumsan. Vivamus interdum ut tortor non sodales. Integer egestas dictum nunc et pharetra. Quisque a luctus mauris. Phasellus nec pretium nisi.</p>
  <div class="btn btn-fill" style="left:629px;top:373px;width:144px;height:39px">Read More</div>

  <div class="meta" style="left:95px;top:539px">DEC. 10, 2020 &nbsp;|&nbsp; POSTED BY LOREM</div>
  <div class="post-title" style="left:95px;top:559px">Vestibulum vel dolor sed lacus lobortis</div>
  <p class="para" style="left:95px;top:604px">Phasellus dapibus tincidunt diam in convallis. Nam ac augue sem. Maecenas consectetur magna eget urna eleifend accumsan. Vivamus interdum ut tortor non sodales. Integer egestas dictum nunc et pharetra. Quisque a luctus mauris. Phasellus nec pretium nisi.</p>
  <div class="btn btn-fill" style="left:95px;top:728px;width:144px;height:41px">Read More</div>
  <div class="photo" role="img" aria-label="Two colleagues reviewing financial charts" style="left:602px;top:477px;width:505px;height:355px;background:linear-gradient(120deg,#3a3836,#7b736a 45%,#c9c4bc)"></div>

  <div class="btn btn-line" style="left:509px;top:864px;width:182px;height:43px">View All Blog</div>
</section>

<section class="team">
  <div class="eyebrow" style="top:35px">Team</div>
  <div class="title" style="top:63px">Meet Our Team</div>

  <div class="member" style="position:absolute;left:132px;top:0;width:200px;height:539px">
    <div class="bracket" style="left:0"></div>
    <div class="photo" role="img" aria-label="Portrait of team member" style="left:13px;top:125px;width:175px;height:199px;background:linear-gradient(180deg,#e6e8ea,#b7bcc2 60%,#2c3036)"></div>
    <div class="name">Lorem Ipsum</div><div class="role">CEO</div>
    <p>Phasellus dapibus tincidunt diam in convallis. Nam ac augue sem.</p>
  </div>
  <div class="member" style="position:absolute;left:377px;top:0;width:200px;height:539px">
    <div class="bracket" style="left:0"></div>
    <div class="photo" role="img" aria-label="Portrait of team member" style="left:13px;top:125px;width:175px;height:199px;background:linear-gradient(180deg,#e6e8ea,#b9bcbf 60%,#7d8086)"></div>
    <div class="name">Lorem Ipsum</div><div class="role">CEO</div>
    <p>Phasellus dapibus tincidunt diam in convallis. Nam ac augue sem.</p>
  </div>
  <div class="member" style="position:absolute;left:622px;top:0;width:200px;height:539px">
    <div class="bracket" style="left:0"></div>
    <div class="photo" role="img" aria-label="Portrait of team member" style="left:13px;top:125px;width:175px;height:199px;background:linear-gradient(180deg,#e6e8ea,#b9b5b2 60%,#25262a)"></div>
    <div class="name">Lorem Ipsum</div><div class="role">CEO</div>
    <p>Phasellus dapibus tincidunt diam in convallis. Nam ac augue sem.</p>
  </div>
  <div class="member" style="position:absolute;left:866px;top:0;width:200px;height:539px">
    <div class="bracket" style="left:0"></div>
    <div class="photo" role="img" aria-label="Portrait of team member" style="left:13px;top:125px;width:175px;height:199px;background:linear-gradient(180deg,#e6e8ea,#b3b4b6 60%,#1f2126)"></div>
    <div class="name">Lorem Ipsum</div><div class="role">CEO</div>
    <p>Phasellus dapibus tincidunt diam in convallis. Nam ac augue sem.</p>
  </div>

  <div class="arrow" style="left:568px;background:#4e3a56"><svg width="10" height="14" viewBox="0 0 10 14"><path d="M8 1 2 7l6 6" fill="none" stroke="#fff" stroke-width="1.5"/></svg></div>
  <div class="arrow" style="left:601px;background:var(--pink)"><svg width="10" height="14" viewBox="0 0 10 14"><path d="m2 1 6 6-6 6" fill="none" stroke="#fff" stroke-width="1.5"/></svg></div>
</section>

<section class="contact">
  <div class="photo" role="img" aria-label="Grey street map background" style="inset:0;background:linear-gradient(135deg,#dedede,#cdcdcd 50%,#dadada)"></div>
  <div class="box">
    <div class="eyebrow" style="top:29px;left:0">Contact Us</div>
    <div class="title" style="top:55px;left:0">Get In Touch</div>
    <div class="field" style="left:77px;top:100px;width:299px;height:38px">First Name</div>
    <div class="field" style="left:381px;top:100px;width:300px;height:38px">Last Name</div>
    <div class="field" style="left:77px;top:147px;width:299px;height:38px">Email address</div>
    <div class="field" style="left:381px;top:147px;width:300px;height:38px">Phone</div>
    <div class="field" style="left:77px;top:191px;width:604px;height:113px">Message</div>
    <div class="btn btn-fill" style="left:315px;top:320px;width:128px;height:36px">Send Now</div>
  </div>
  <div class="abs" style="left:573px;top:35px;width:54px;height:54px;border-radius:50%;background:var(--navy);display:flex;align-items:center;justify-content:center">
    <svg width="24" height="17" viewBox="0 0 24 17"><rect x="1" y="1" width="22" height="15" fill="none" stroke="#fff" stroke-width="1.4"/><path d="m1 1 11 9 11-9" fill="none" stroke="#fff" stroke-width="1.4"/></svg>
  </div>
</section>

<section class="footer">
  <h4 style="left:93px">Follow Us</h4>
  <div class="social"><i style="left:94px;top:117px"></i><i style="left:134px;top:117px"></i><i style="left:173px;top:117px"></i><i style="left:213px;top:117px"></i></div>

  <h4 style="left:339px">Quick Links</h4>
  <div class="link" style="left:341px;top:122px">About Us</div>
  <div class="link" style="left:341px;top:157px">Expertise</div>
  <div class="link" style="left:341px;top:193px">Global Outlook</div>
  <div class="link" style="left:341px;top:229px">Sectors</div>
  <div class="link" style="left:461px;top:122px">Management</div>
  <div class="link" style="left:461px;top:157px">Media</div>
  <div class="link" style="left:461px;top:193px">Contact Us</div>

  <h4 style="left:654px">Sectors</h4>
  <div class="link" style="left:654px;top:122px">Real Estate</div>
  <div class="link" style="left:654px;top:148px">E-Commerce</div>
  <div class="link" style="left:654px;top:175px">Healthcare</div>
  <div class="link" style="left:654px;top:202px">Beauty &amp; Personal Care</div>
  <div class="link" style="left:654px;top:229px">Technology</div>
  <div class="link" style="left:654px;top:256px">Resources</div>

  <svg class="abs" style="left:859px;top:80px" width="14" height="10" viewBox="0 0 14 10"><rect width="14" height="10" fill="#fff"/><path d="m0 0 7 5 7-5" fill="none" stroke="#4a2f48" stroke-width="1.2"/></svg>
  <div class="link" style="left:881px;top:77px;font-size:12.5px">Stay update with us</div>
  <div class="abs" style="left:859px;top:115px;width:247px;height:34px;background:#fff;color:#888;font-size:11px;font-weight:300;padding:10px 12px">Enter your Email address</div>
  <div class="btn btn-fill" style="left:977px;top:163px;width:129px;height:34px;font-size:10.5px">Subscribe</div>

  <div class="rule"></div>
  <div class="copy">© 2020 <span style="color:#fff;font-weight:500">Harbor Stone Partners</span> All Right Reserved.</div>
</section>

</body>
</html>
```